Packaging design for a revolutionary hi-protein snack of Norwegian salmon

We need a breathtaking packing design for a smal snack bag (30 g) for a revolutionary new hi-protein snack made of Norwegian salmon. The product will be made with two different flavors; MANGO and WASABI. The product is extreme high in protein (60%) and omega 3, and are just natural.

We want to see a bold and fresh design that appeals to protein lovers of all ages.

Target Market(s)

Our target market is boys and girls that are 18-35 years old and that are interested in working out and eating healthy.

Industry/Entity Type

Snack industry (functional food, healthy snack, protein snack)

Font styles to use
Sans Serif

Requirements
Must have
• The package design must give the customer a WOW feeling. "HI-PROTEIN SNACK" must be highligted. Further, the design must use the Tidal Compass setup (attached).

```html
<!DOCTYPE html>
<html lang="en">
<head>
<meta charset="utf-8">
<title>Hi Protein Snack – Mango flavor</title>
<link href="https://fonts.googleapis.com/css2?family=Fredoka:wght@600;700&family=Oswald:wght@400&family=Raleway:wght@400&family=Roboto:wght@700&family=Tinos&display=swap" rel="stylesheet">
<style>
  :root{
    --stage:#141414;
    --bag:#121111;
    --crimp-dark:#2a1a10;
    --crimp-warm:#b5531c;
    --white:#ffffff;
    --yellow:#f6cc12;
    --green:#22d33a;
    --badge-green:#1fe84c;
    --band-red:#d9461a;
    --band-text:#3a140a;
    --mango-light:#f7a640;
    --mango-deep:#e0541a;
  }
  *{margin:0;padding:0;box-sizing:border-box}
  html,body{width:1200px;height:933px;overflow:hidden;background:var(--stage)}
  .canvas{position:relative;width:1200px;height:933px;background:var(--stage)}
  .bag{position:absolute;left:381px;top:112px;width:438px;height:706px;background:var(--bag);overflow:hidden;border-radius:3px}
  .crimp{position:absolute;left:0;width:100%;background:linear-gradient(90deg,var(--crimp-dark),var(--crimp-warm) 18%,var(--crimp-dark) 35%,#8a3d14 55%,var(--crimp-dark) 72%,var(--crimp-warm) 90%,var(--crimp-dark))}
  .crimp--top{top:0;height:72px}
  .crimp--bottom{bottom:0;height:30px;background:#0b0b0b;z-index:1}
  .hang-hole{position:absolute;left:176px;top:33px;width:91px;height:14px;border-radius:7px;background:var(--stage)}
  .photo{position:absolute;border-radius:38% 46% 42% 50%;background:radial-gradient(circle at 45% 40%,var(--mango-light),var(--mango-deep) 70%,#a8320c)}
  .photo--hero{left:91px;top:429px;width:253px;height:206px}
  .photo--corner{left:338px;top:127px;width:77px;height:71px;border-radius:30% 50% 35% 45%}
  .photo--side-left{left:-30px;top:265px;width:60px;height:120px;opacity:.55}
  .photo--side-right{left:410px;top:420px;width:50px;height:110px;opacity:.45}
  .brand{position:absolute;left:44px;top:165px;font-family:"Fredoka",sans-serif;font-weight:700;font-size:22px;line-height:1;color:var(--white);display:flex;align-items:center;gap:6px}
  .brand-dot{width:10px;height:10px;border-radius:50%;background:var(--white)}
  .headline{position:absolute;left:0;width:100%;text-align:center;padding-left:10px}
  .headline--hi{top:192px;font-family:"Fredoka",sans-serif;font-weight:700;font-size:54px;line-height:50px;color:var(--white)}
  .headline--protein{top:246px;font-family:"Fredoka",sans-serif;font-weight:700;font-size:66px;line-height:60px;letter-spacing:1px;color:var(--yellow)}
  .headline--snack{top:306px;font-family:"Oswald",sans-serif;font-size:34px;line-height:36px;color:var(--white)}
  .flavor{position:absolute;left:0;width:100%;top:348px;text-align:center;font-family:"Raleway",sans-serif;font-size:48px;line-height:54px;color:var(--green);padding-left:20px}
  .claim-band{position:absolute;left:0;top:642px;width:360px;height:32px;background:var(--band-red);font-family:"Tinos",serif;font-size:19px;line-height:32px;color:var(--band-text);padding-left:14px;white-space:nowrap;z-index:2}
  .weight-badge{position:absolute;left:365px;top:625px;width:58px;height:76px;background:var(--badge-green);text-align:center;font-family:"Roboto",sans-serif;font-weight:700;color:#0c1a0c;z-index:3}
  .weight-badge__label{display:block;margin-top:9px;font-size:8px;font-style:italic;line-height:11px}
  .weight-badge__value{display:block;font-size:22px;line-height:26px;margin-top:8px}
</style>
</head>
<body>
<div class="canvas">
  <div class="bag">
    <div class="crimp crimp--top" role="img" aria-label="Woven orange and black stripe pattern along the top seal"></div>
    <div class="hang-hole"></div>

    <div class="photo photo--side-left" role="img" aria-label="Blurred dried salmon piece at the left edge"></div>
    <div class="photo photo--side-right" role="img" aria-label="Blurred dried salmon piece at the right edge"></div>
    <div class="photo photo--corner" role="img" aria-label="Single mango-glazed salmon chip"></div>

    <div class="brand"><span class="brand-dot"></span>Tidal Compass</div>

    <h1 class="headline headline--hi">HI</h1>
    <p class="headline headline--protein">PROTEIN</p>
    <p class="headline headline--snack">SNACK</p>
    <p class="flavor">Mango flavor</p>

    <div class="photo photo--hero" role="img" aria-label="Pile of mango-glazed dried salmon chips"></div>

    <div class="claim-band">PROTEIN (60%) AND OMEGA 3,</div>
    <div class="crimp crimp--bottom"></div>

    <div class="weight-badge">
      <span class="weight-badge__label">NET<br>WEIGHT</span>
      <span class="weight-badge__value">30g</span>
    </div>
  </div>
</div>
</body>
</html>
```